Design some Business Cards

Thank you so much for viewing my contest ! Please be creative
I need some business cards with a cool design, simple and professional.
Below i will add 2 Logos. I want a matte black Background Entry, and a white background entry both front and back. PLEASE KEEP ORIGINAL LOGO COLORS
Please add to the back of the card
Service/Repair/Installations
Duct cleaning services
Miami Dade/Broward County
Call now for a free quote
Special Duct Cleaning Prices
I will need to include contact info for example:
Instagram
Email
Phone Number
Thank you any questions feel free to contact me.!
I appreciate any creative work!

```html
<!DOCTYPE html>
<html lang="en">
<head>
<meta charset="UTF-8">
<title>Coolbreeze Climate — Business Cards</title>
<link href="https://fonts.googleapis.com/css2?family=Montserrat:wght@400;600;800&display=swap" rel="stylesheet">
<style>
  :root {
    --blue: #2b7399;
    --blue-dark: #1c5576;
    --ink: #1f2a33;
    --white: #ffffff;
    --page: #e9ecef;
    --shadow: rgba(0,0,0,0.18);
  }
  * { margin: 0; padding: 0; box-sizing: border-box; }
  html, body { width: 1200px; height: 900px; overflow: hidden; }
  body {
    background: var(--page);
    font-family: 'Montserrat', sans-serif;
    position: relative;
  }
  .card {
    position: absolute;
    left: 250px;
    width: 700px;
    height: 400px;
    background: var(--white);
    overflow: hidden;
    box-shadow: 0 6px 20px var(--shadow);
  }
  .card--front { top: 40px; }
  .card--back { top: 460px; }

  /* Front */
  .front-band {
    position: absolute; left: 0; top: 0;
    width: 190px; height: 100%;
    background: var(--blue);
  }
  .teeth-vertical {
    position: absolute; left: 190px; top: 0;
    width: 14px; height: 100%;
    background: repeating-linear-gradient(to bottom, var(--blue) 0 14px, transparent 14px 28px);
  }
  .front-stripe {
    position: absolute;
    left: 0;
    height: 8px;
    background: var(--white);
    transform: skewY(-8deg);
    transform-origin: left;
  }
  .brand {
    position: absolute;
    display: flex; align-items: center; gap: 14px;
  }
  .brand__mark {
    width: 44px; height: 44px; border-radius: 50%;
    background: var(--blue);
  }
  .brand__name {
    font-weight: 800;
    color: var(--blue);
    text-transform: uppercase;
    letter-spacing: 1px;
  }
  .card--front .brand { left: 260px; top: 175px; }
  .card--front .brand__name { font-size: 28px; }

  /* Back */
  .back-band-top {
    position: absolute; left: 0; top: 0; width: 100%; height: 62px;
    background: var(--blue);
  }
  .back-band-bottom {
    position: absolute; left: 0; bottom: 0; width: 100%; height: 72px;
    background: var(--blue);
  }
  .teeth-horizontal {
    position: absolute; left: 0; width: 100%; height: 14px;
    background: repeating-linear-gradient(to right, var(--blue) 0 14px, transparent 14px 30px);
  }
  .teeth-horizontal--top { top: 62px; }
  .teeth-horizontal--bottom { bottom: 72px; }
  .name-tag {
    position: absolute; left: 36px; top: 28px;
    background: var(--blue-dark);
    color: var(--white);
    padding: 8px 26px 8px 18px;
    box-shadow: 0 3px 6px var(--shadow);
  }
  .name-tag__name { font-size: 17px; font-weight: 800; letter-spacing: 2px; }
  .name-tag__role { font-size: 10px; font-weight: 400; letter-spacing: 1px; margin-top: 2px; }
  .card--back .brand { left: 50px; top: 180px; gap: 10px; }
  .card--back .brand__mark { width: 32px; height: 32px; }
  .card--back .brand__name { font-size: 15px; }
  .divider {
    position: absolute; left: 330px; top: 130px;
  }
  .contact {
    position: absolute; right: 36px; top: 120px;
    width: 250px;
    font-size: 12.5px;
    color: var(--ink);
    text-align: right;
  }
  .contact__row {
    display: flex; justify-content: flex-end; align-items: center; gap: 12px;
    padding: 6px 0;
    border-bottom: 1.5px solid var(--blue);
  }
  .contact__row:last-child { border-bottom: none; }
  .contact__text { line-height: 1.45; }
  .contact__icon { width: 14px; height: 14px; flex: none; }
</style>
</head>
<body>

<section class="card card--front" aria-label="Card front">
  <div class="front-band"></div>
  <div class="teeth-vertical"></div>
  <div class="front-stripe" style="top:60px;width:170px"></div>
  <div class="front-stripe" style="top:100px;width:175px"></div>
  <div class="front-stripe" style="top:140px;width:180px"></div>
  <div class="front-stripe" style="top:285px;width:170px"></div>
  <div class="front-stripe" style="top:325px;width:175px"></div>
  <div class="front-stripe" style="top:365px;width:180px"></div>
  <div class="brand">
    <span class="brand__mark"></span>
    <span class="brand__name">Coolbreeze Climate</span>
  </div>
</section>

<section class="card card--back" aria-label="Card back">
  <div class="back-band-top"></div>
  <div class="teeth-horizontal teeth-horizontal--top"></div>
  <div class="back-band-bottom"></div>
  <div class="teeth-horizontal teeth-horizontal--bottom"></div>

  <div class="name-tag">
    <div class="name-tag__name">DANIEL REYES</div>
    <div class="name-tag__role">Managing Director</div>
  </div>

  <div class="brand">
    <span class="brand__mark"></span>
    <span class="brand__name">Coolbreeze Climate</span>
  </div>

  <svg class="divider" width="40" height="150" viewBox="0 0 40 150">
    <line x1="14" y1="0" x2="8" y2="150" stroke="#2b7399" stroke-width="2"/>
    <line x1="26" y1="0" x2="20" y2="150" stroke="#2b7399" stroke-width="2"/>
  </svg>

  <div class="contact">
    <div class="contact__row">
      <div class="contact__text">+000 123 345 678<br>+000 123 345 678</div>
      <svg class="contact__icon" viewBox="0 0 24 24"><path fill="#1c5576" d="M6.6 10.8a15 15 0 0 0 6.6 6.6l2.2-2.2c.3-.3.7-.4 1-.2 1.1.4 2.3.6 3.6.6.6 0 1 .4 1 1V20c0 .6-.4 1-1 1A17 17 0 0 1 3 4c0-.6.4-1 1-1h3.5c.6 0 1 .4 1 1 0 1.3.2 2.5.6 3.6.1.3 0 .7-.2 1z"/></svg>
    </div>
    <div class="contact__row">
      <div class="contact__text">hello@coolbreezeclimate.com<br>info@coolbreezeclimate.com</div>
      <svg class="contact__icon" viewBox="0 0 24 24"><rect x="2" y="5" width="20" height="14" rx="1" fill="#1c5576"/><path d="M3 6l9 7 9-7" stroke="#fff" stroke-width="1.6" fill="none"/></svg>
    </div>
    <div class="contact__row">
      <div class="contact__text">your location<br>street, country.</div>
      <svg class="contact__icon" viewBox="0 0 24 24"><path fill="#1c5576" d="M12 2a7 7 0 0 0-7 7c0 5 7 13 7 13s7-8 7-13a7 7 0 0 0-7-7zm0 9.5A2.5 2.5 0 1 1 12 6.5a2.5 2.5 0 0 1 0 5z"/></svg>
    </div>
  </div>
</section>

</body>
</html>
```